Logo, letterhead and business card for new counseling business

Looking for a clean and professional design. The name of the business is Clearwater Counseling, PLLC with a website of www.clearwatercounselingnw.com We specialize in working with adolescents and families. We are looking for a logo that exudes confidence, trust, hope, compassion. I am excited to open my new business and help families get better, overcome their issues and enjoy their lives more. I have spent the past 9 years working for others and it is time for me to make my own way. I have strong ethics so people can trust me. I care for the people I serve. I need a logo to go along with my strong business name to help me stand out even though I am just starting my business.

Target Market(s)

Adolescent and families who are struggling emotionally or have addiction issues.

Industry/Entity Type

Business

Contact Information for Business Card

Clearwater Counseling, PLLC
4827 Birchwood Lane, Suite 310, Maple Grove, Minnesota, 55369
(612)555-0143
dana@clearwatercounselingnw.com
clearwatercounselingnw.com

Logo Text

Clearwater Counseling

Logo styles of interest
Emblem Logo
Pictorial/Combination Logo
Wordmark Logo
Font styles to use
Serif
Sans Serif

Requirements
Must have
• Clean, professional design.
Nice to have
• I want the design to feel trustworthy and safe. Dependable.
Should not have
• childish fonts

```html
<!DOCTYPE html>
<html lang="en">
<head>
<meta charset="utf-8">
<title>Clearwater Counseling — Identity Set</title>
<link rel="stylesheet" href="https://fonts.googleapis.com/css2?family=Tinos:wght@400;700&display=swap">
<style>
  :root {
    --ink: #000000;
    --paper: #ffffff;
    --grey-dark: #5a5a5a;
    --grey-mid: #9a9a9a;
    --grey-light: #e6e6e6;
    --faint: rgba(0, 0, 0, 0.10);
  }
  * { box-sizing: border-box; margin: 0; padding: 0; }
  html, body { width: 820px; height: 1200px; overflow: hidden; background: var(--paper); }
  body { font-family: "Tinos", "Times New Roman", serif; color: var(--ink); }
  .sheet { position: relative; width: 820px; height: 1200px; overflow: hidden; }

  /* Business card — back */
  .card-back {
    position: absolute; left: 352px; top: -28px; width: 460px; height: 262px;
    transform: rotate(3deg); transform-origin: top left;
    background: linear-gradient(115deg, var(--grey-dark) 0%, var(--grey-mid) 22%, var(--grey-light) 48%, var(--paper) 70%);
    box-shadow: 0 0 0 1px var(--grey-light);
  }
  .card-back .watermark {
    position: absolute; left: 40px; top: 100px; width: 390px; text-align: center;
    font-size: 36px; color: var(--faint); line-height: 1; white-space: nowrap;
  }
  .card-back .definition {
    position: absolute; left: 80px; top: 40px; width: 320px; text-align: center;
    font-size: 12.5px; line-height: 1.3;
  }
  .card-back .definition strong { font-weight: 700; }
  .card-back .promise {
    position: absolute; left: 30px; top: 226px; width: 420px; text-align: right;
    font-size: 9px; white-space: nowrap;
  }

  /* Business card — front */
  .card-front {
    position: absolute; left: 42px; top: 168px; width: 335px; height: 240px;
    transform: rotate(-16deg); transform-origin: top left;
    background: var(--paper); box-shadow: 0 0 0 1px var(--grey-light);
    overflow: hidden;
  }
  .card-front .shade {
    position: absolute; inset: 0;
    background: linear-gradient(100deg, var(--grey-mid) 0%, var(--grey-light) 40%, var(--paper) 75%);
    clip-path: polygon(0 0, 100% 0, 100% 62%, 0 100%);
  }
  .card-front .band {
    position: absolute; left: 0; bottom: 0; width: 64%; height: 44%;
    background: var(--ink);
    clip-path: polygon(0 20%, 100% 0, 100% 100%, 0 100%);
  }
  .card-front .holder {
    position: absolute; left: 18px; bottom: 22px; color: var(--paper);
    font-size: 17px; line-height: 1.2;
  }
  .card-front .mark {
    position: absolute; left: 0; top: 26px; width: 100%; text-align: center;
    font-size: 21px; white-space: nowrap;
  }
  .card-front .rule { position: absolute; left: 50px; right: 40px; height: 1px; background: var(--ink); }
  .card-front .tag { position: absolute; left: 0; top: 68px; width: 100%; text-align: center; font-size: 12px; }
  .card-front .services {
    position: absolute; left: 24px; top: 96px; width: 290px; text-align: center;
    font-size: 7px; line-height: 1.35;
  }
  .card-front .services b { font-weight: 700; }
  .card-front .contact {
    position: absolute; right: 14px; top: 132px; text-align: left;
    font-size: 14px; line-height: 1.15;
  }

  /* Primary logo */
  .logo-primary { position: absolute; left: 476px; top: 400px; width: 336px; }
  .logo-primary .name {
    text-align: center; font-size: 34px; line-height: 1; padding-top: 60px; white-space: nowrap;
  }
  .logo-primary .rule { height: 2px; background: var(--ink); }
  .logo-primary .tagline { text-align: center; font-size: 19px; padding: 4px 0 3px; }

  /* Letterhead */
  .letterhead {
    position: absolute; left: 90px; top: 612px; width: 480px; height: 588px;
    background: var(--paper); border: 1px solid var(--ink); border-left: 9px solid var(--ink);
  }
  .letterhead .mark { text-align: center; font-size: 18px; margin-top: 28px; }
  .letterhead .rule { height: 1.5px; background: var(--ink); margin: 0 22px; }
  .letterhead .details { text-align: center; font-size: 9px; line-height: 1.2; padding: 2px 0 4px; }
</style>
</head>
<body>
<main class="sheet">

  <section class="card-back" aria-label="Business card back">
    <div class="watermark" aria-hidden="true">Clearwater Counseling</div>
    <p class="definition">
      <strong>Mental or emotional health</strong><br>
      refers to your overall psychological well-being.<br>
      It includes the way you feel about yourself,<br>
      the quality of your relationships,<br>
      and your ability to manage your feelings<br>
      and deal with difficulties.
    </p>
    <p class="promise">Clearwater Counseling, PLLC. Professional, caring help for the challenging times in your life.</p>
  </section>

  <section class="card-front" aria-label="Business card front">
    <div class="shade"></div>
    <div class="mark">Clearwater Counseling</div>
    <div class="rule" style="top:60px"></div>
    <div class="tag">Clearwater Counseling</div>
    <div class="rule" style="top:86px"></div>
    <p class="services">
      We help you at whatever stage you are in and in the manner most comfortable for you.<br>
      <b>Self-help tools...email/text therapy...phone therapy...video therapy...in person therapy</b>
    </p>
    <div class="contact">Phone<br>Address<br>e_mail</div>
    <div class="band"></div>
    <div class="holder">Name:<br>Profession</div>
  </section>

  <section class="logo-primary" aria-label="Primary logo">
    <div class="name">Clearwater Counseling</div>
    <div class="rule" style="margin-top:50px"></div>
    <div class="tagline">Clearwater Counseling</div>
    <div class="rule"></div>
  </section>

  <section class="letterhead" aria-label="Letterhead">
    <div class="mark">Clearwater Counseling</div>
    <div class="rule" style="margin-top:8px"></div>
    <div class="details">Address<br>Phone</div>
    <div class="rule"></div>
  </section>

</main>
</body>
</html>
```